Templates for Construction Company

We are looking to have templates prepared for all aspects of our letter sending. Using our brand design. with similar layouts that look the same.

Letterheads design & Email signatures

We use letter heads for - quotes, contract correspondence, variations, formal letters, invitations

Target Market(s)

Clients documents sent in emails

Industry/Entity Type

Construction

Font styles to use
Serif
Sans Serif

Colors
0054AA
0677BA
7BADD7
CADEEF
E8F1F8

Requirements
Must have
• Easy to read, water marks on page
Nice to have
• Different options for different letters

```html
<!DOCTYPE html>
<html lang="en">
<head>
<meta charset="utf-8">
<title>Stonefield Building Group – Letterhead &amp; Email Signature</title>
<link href="https://fonts.googleapis.com/css2?family=Roboto+Condensed:wght@700&family=Roboto:wght@700&display=swap" rel="stylesheet">
<style>
  :root {
    --brand-blue: #5a88c6;
    --brand-grey: #5a5a5a;
    --text-dark: #444444;
    --paper: #ffffff;
    --watermark: #eef3fa;
    --bg-top: #88aad8;
    --bg-mid: #bdd1ea;
    --bg-bottom: #6590c9;
  }
  * { margin: 0; padding: 0; box-sizing: border-box; }
  html, body { width: 1200px; height: 750px; overflow: hidden; }
  body {
    position: relative;
    background: linear-gradient(180deg, var(--bg-top) 0%, var(--bg-mid) 40%, var(--bg-bottom) 100%);
    font-family: "Roboto Condensed", "Arial Narrow", sans-serif;
    color: var(--text-dark);
  }
  .section-label {
    position: absolute;
    font-weight: 700;
    color: var(--text-dark);
    border-bottom: 2px solid var(--text-dark);
    line-height: 1.2;
    padding-bottom: 3px;
    font-size: 19px;
  }
  .section-label--letterhead { left: 120px; top: 58px; }
  .section-label--signature { left: 642px; top: 288px; }

  .letterhead {
    position: absolute;
    left: 120px; top: 95px;
    width: 438px; height: 595px;
    background: var(--paper);
    box-shadow: 0 6px 14px rgba(40, 60, 100, 0.35);
  }
  .signature {
    position: absolute;
    left: 640px; top: 325px;
    width: 499px; height: 135px;
    background: var(--paper);
    box-shadow: 0 6px 14px rgba(40, 60, 100, 0.35);
  }

  .brand {
    position: absolute;
    display: flex;
    align-items: center;
    gap: 7px;
    font-family: "Roboto", Arial, sans-serif;
    font-weight: 700;
    font-size: 30px;
    line-height: 1;
    color: var(--brand-blue);
    letter-spacing: -0.5px;
    white-space: nowrap;
  }
  .brand__square { width: 18px; height: 18px; background: var(--brand-blue); flex: none; }
  .letterhead .brand { left: 30px; top: 42px; }
  .signature .brand { left: 18px; top: 46px; }

  .watermark {
    position: absolute;
    left: 40px; top: 265px;
    width: 358px;
    text-align: center;
    font-family: "Roboto", Arial, sans-serif;
    font-weight: 700;
    font-size: 70px;
    color: var(--watermark);
    letter-spacing: -1px;
  }

  .contact-list { position: absolute; list-style: none; font-weight: 700; white-space: nowrap; }
  .contact-list li { display: flex; align-items: flex-start; }
  .contact-list svg { flex: none; }
  .letterhead .contact-list { left: 236px; top: 18px; font-size: 11.5px; line-height: 14px; }
  .letterhead .contact-list li { margin-bottom: 10px; gap: 6px; }
  .letterhead .contact-list svg { width: 17px; height: 15px; }
  .signature .contact-list { left: 225px; top: 24px; font-size: 15px; line-height: 20px; }
  .signature .contact-list li { margin-bottom: 8px; gap: 11px; }
  .signature .contact-list svg { width: 20px; height: 19px; margin-top: 1px; }

  .footer-bands { position: absolute; left: 0; bottom: 0; width: 100%; }
  .footer-bands span { position: absolute; top: 0; height: 100%; }
  .letterhead .footer-bands { height: 19px; }
  .signature .footer-bands { height: 14px; }
  .band--grey { background: var(--brand-grey); }
  .band--blue { background: var(--brand-blue); }
</style>
</head>
<body>

  <h2 class="section-label section-label--letterhead">Letterhead</h2>

  <section class="letterhead">
    <div class="brand"><span class="brand__square"></span>Stonefield</div>

    <ul class="contact-list">
      <li>
        <svg viewBox="0 0 20 14"><rect x="0.5" y="0.5" width="19" height="13" fill="var(--brand-blue)"/><path d="M0.5 0.5 L10 8 L19.5 0.5 M0.5 13.5 L7.5 6.5 M19.5 13.5 L12.5 6.5" stroke="#fff" stroke-width="1.3" fill="none"/></svg>
        hello@stonefieldbuild.com
      </li>
      <li>
        <svg viewBox="0 0 20 20"><circle cx="10" cy="10" r="9" fill="none" stroke="var(--brand-blue)" stroke-width="1.6"/><ellipse cx="10" cy="10" rx="4" ry="9" fill="none" stroke="var(--brand-blue)" stroke-width="1.4"/><path d="M1 10 H19 M2.5 5.5 H17.5 M2.5 14.5 H17.5 M10 1 V19" stroke="var(--brand-blue)" stroke-width="1.4"/></svg>
        www.stonefieldbuild.group
      </li>
      <li>
        <svg viewBox="0 0 20 20"><circle cx="10" cy="10" r="10" fill="var(--brand-blue)"/><path d="M7 5 L8.8 5.2 L9.4 8 L8.3 9 C8.9 10.4 9.8 11.3 11.1 11.8 L12.1 10.7 L14.8 11.3 L15 13.1 C13.8 14.6 11.6 14.7 9.4 13.1 C7.4 11.6 5.7 9 5.7 7 C5.8 6 6.3 5.4 7 5 Z" fill="#fff"/></svg>
        55501 24680
      </li>
      <li>
        <svg viewBox="0 0 20 24"><path d="M10 1 C5 1 2 4.5 2 8.6 C2 14 10 23 10 23 C10 23 18 14 18 8.6 C18 4.5 15 1 10 1 Z" fill="var(--brand-blue)"/><circle cx="10" cy="8.6" r="3" fill="#fff"/></svg>
        <span>48 Harbour Lane, Riverton Park<br>Westbrook District. pin 7042195</span>
      </li>
    </ul>

    <div class="watermark" aria-hidden="true">Stonefield</div>

    <div class="footer-bands">
      <span class="band--grey" style="left:0;width:141px"></span>
      <span class="band--blue" style="left:146px;width:148px"></span>
      <span class="band--grey" style="left:299px;width:139px"></span>
    </div>
  </section>

  <h2 class="section-label section-label--signature">Email signature</h2>

  <section class="signature">
    <div class="brand"><span class="brand__square"></span>Stonefield</div>

    <ul class="contact-list">
      <li>
        <svg viewBox="0 0 20 14"><rect x="0.5" y="0.5" width="19" height="13" fill="var(--brand-blue)"/><path d="M0.5 0.5 L10 8 L19.5 0.5 M0.5 13.5 L7.5 6.5 M19.5 13.5 L12.5 6.5" stroke="#fff" stroke-width="1.3" fill="none"/></svg>
        hello@stonefieldbuild.com
      </li>
      <li>
        <svg viewBox="0 0 20 20"><circle cx="10" cy="10" r="9" fill="none" stroke="var(--brand-blue)" stroke-width="1.6"/><ellipse cx="10" cy="10" rx="4" ry="9" fill="none" stroke="var(--brand-blue)" stroke-width="1.4"/><path d="M1 10 H19 M2.5 5.5 H17.5 M2.5 14.5 H17.5 M10 1 V19" stroke="var(--brand-blue)" stroke-width="1.4"/></svg>
        www.stonefieldbuild.group
      </li>
      <li>
        <svg viewBox="0 0 20 20"><circle cx="10" cy="10" r="10" fill="var(--brand-blue)"/><path d="M7 5 L8.8 5.2 L9.4 8 L8.3 9 C8.9 10.4 9.8 11.3 11.1 11.8 L12.1 10.7 L14.8 11.3 L15 13.1 C13.8 14.6 11.6 14.7 9.4 13.1 C7.4 11.6 5.7 9 5.7 7 C5.8 6 6.3 5.4 7 5 Z" fill="#fff"/></svg>
        55501 24680
      </li>
    </ul>

    <div class="footer-bands">
      <span class="band--grey" style="left:0;width:158px"></span>
      <span class="band--blue" style="left:164px;width:184px"></span>
      <span class="band--grey" style="left:354px;width:145px"></span>
    </div>
  </section>

</body>
</html>
```